" Trata-se de uma clínica em início de funcionamento. Somos dois responsáveis técnicos (Psicólogos) e temos outros seis profissionais que estarão trabalhando conosco (também psicólogos). Temos uma médica Psiquiatra que fará parte da equipe. Ofereceremos atendimento nas abordagens: terapia cognitivo comportamental, humanista, psicanálise e Gestalt, entretanto, o foco será na Terapia Cognitivo-Comportamental (TCC). De forma breve, a base da TCC é: Nossos pensamentos, emoções e comportamentos estão interligados e influenciam um ao outro e são o foco principal do tratamento. Fazemos atendimentos individuais e em grupo. Além dos atendimentos de psicologia, a nossa proposta é oferecer outros serviços como palestras, cursos, treinamentos. Disponibilizamos de auditório para uso da clínica. No meu caso, tenho forte vínculo acadêmico. Sou pesquisadora do Núcleo de Estudos Clínicos da UNEVAR e faço mestrado em Saúde Mental na mesma instituição. Também pós-graduanda em TCC. Então o ensino será algo que terá um investimento forte, juntamente com os atendimentos clínicos. "

```html
<!DOCTYPE html>
<html lang="pt-BR">
<head>
<meta charset="UTF-8">
<title>Mentara — assinaturas de e-mail</title>
<link href="https://fonts.googleapis.com/css2?family=Open+Sans:wght@400;700&display=swap" rel="stylesheet">
<style>
  :root{
    --navy:#0f2a4a;
    --navy-soft:#1d4064;
    --teal:#5fb3ad;
    --white:#ffffff;
    --stage:#e3e3e3;
    --stage-edge:#cfcfcf;
    --ink:#0f2a4a;
  }
  *{box-sizing:border-box;margin:0;padding:0}
  html,body{width:1200px;height:1200px;overflow:hidden}
  body{
    background:radial-gradient(circle at 50% 45%,#f1f1f1 0%,var(--stage) 60%,var(--stage-edge) 100%);
    font-family:"Open Sans",Arial,sans-serif;
    position:relative;
  }
  .signature{position:absolute;left:125px;width:950px;height:257px;overflow:hidden}
  .signature--light{top:312px;background:var(--white)}
  .signature--dark{top:624px;height:264px;background:var(--navy)}

  .pattern-field{
    position:absolute;inset:0;
    background:radial-gradient(ellipse at 30% 40%,var(--navy-soft) 0%,var(--navy) 70%);
  }
  .signature--light .pattern-field{right:auto;width:530px;clip-path:polygon(0 0,100% 0,77% 100%,0 100%)}
  .accent-stripe{position:absolute;top:0;left:0;width:100%;height:100%}

  .brand{position:absolute;display:flex;align-items:center;gap:14px;color:var(--white)}
  .brand__dot{width:48px;height:48px;border-radius:50%;background:var(--teal);flex:none}
  .brand__name{font-weight:700;font-size:34px;line-height:1}
  .signature--light .brand{left:44px;top:104px}
  .signature--dark .brand{left:44px;top:113px}

  .person{position:absolute;text-align:right;color:var(--ink);line-height:1}
  .person__name{font-weight:700;font-size:22px}
  .person__role{font-weight:700;font-size:11px;margin-top:3px}
  .signature--light .person{right:38px;top:24px}
  .signature--dark .person{left:300px;top:114px;width:242px;color:var(--white)}

  .divider{position:absolute;left:614px;top:72px;width:3px;height:132px;background:var(--white)}

  .contacts{position:absolute;list-style:none;display:flex;flex-direction:column;align-items:flex-end}
  .contacts li{display:flex;align-items:center;gap:10px;font-weight:700;font-size:16px;height:36px}
  .signature--light .contacts{right:26px;top:70px;color:var(--ink)}
  .signature--dark .contacts{right:26px;top:72px;color:var(--white)}
  .icon{width:24px;height:24px;flex:none;fill:var(--teal);stroke:var(--teal)}

  .base-band{position:absolute;left:0;bottom:0;width:100%;height:16px;background:var(--teal)}
</style>
</head>
<body>
<svg width="0" height="0" style="position:absolute" aria-hidden="true">
  <defs>
    <symbol id="i-phone" viewBox="0 0 24 24">
      <circle cx="12" cy="12" r="11" fill="none" stroke-width="1.6"/>
      <path d="M8.6 10.6a9 9 0 0 0 4.8 4.8l1.5-1.5a.7.7 0 0 1 .7-.2 7 7 0 0 0 2.2.4.7.7 0 0 1 .7.7v2.2a.7.7 0 0 1-.7.7A11 11 0 0 1 6.3 6.5a.7.7 0 0 1 .7-.7h2.2a.7.7 0 0 1 .7.7c0 .8.1 1.5.4 2.2a.7.7 0 0 1-.2.7z" stroke="none"/>
    </symbol>
    <symbol id="i-social" viewBox="0 0 24 24">
      <circle cx="12" cy="12" r="11" stroke="none"/>
    </symbol>
    <symbol id="i-pin" viewBox="0 0 24 24">
      <circle cx="12" cy="12" r="11" stroke="none"/>
      <path d="M12 5.5a4.3 4.3 0 0 0-4.3 4.3c0 3.2 4.3 8.2 4.3 8.2s4.3-5 4.3-8.2A4.3 4.3 0 0 0 12 5.5zm0 5.9a1.6 1.6 0 1 1 0-3.2 1.6 1.6 0 0 1 0 3.2z" fill="#fff" stroke="none"/>
    </symbol>
    <symbol id="i-web" viewBox="0 0 24 24">
      <circle cx="12" cy="12" r="11" stroke="none"/>
      <g fill="none" stroke="#fff" stroke-width="1.3">
        <circle cx="12" cy="12" r="6"/>
        <ellipse cx="12" cy="12" rx="2.6" ry="6"/>
        <path d="M6 12h12"/>
      </g>
    </symbol>
  </defs>
</svg>

<section class="signature signature--light">
  <div class="pattern-field" role="img" aria-label="Fundo azul-marinho com padrão decorativo de círculos translúcidos"></div>
  <svg class="accent-stripe" viewBox="0 0 950 257" preserveAspectRatio="none" aria-hidden="true">
    <polygon points="545,0 566,0 451,257 430,257" fill="var(--teal)"/>
  </svg>
  <div class="brand">
    <span class="brand__dot"></span>
    <span class="brand__name">Mentara</span>
  </div>
  <div class="person">
    <p class="person__name">Nome Sobrenome</p>
    <p class="person__role">cargo</p>
  </div>
  <ul class="contacts">
    <li>+55 21 3210-4780 <svg class="icon"><use href="#i-phone"/></svg></li>
    <li>+55 21 98765-1402 <svg class="icon"><use href="#i-phone"/></svg></li>
    <li>/clinicamentara <svg class="icon"><use href="#i-social"/></svg></li>
    <li>R. Aurora Nº 24 - centro <svg class="icon"><use href="#i-pin"/></svg></li>
    <li>mentara.com.br <svg class="icon"><use href="#i-web"/></svg></li>
  </ul>
</section>

<section class="signature signature--dark">
  <div class="pattern-field" role="img" aria-label="Fundo azul-marinho com padrão decorativo de círculos translúcidos"></div>
  <div class="brand">
    <span class="brand__dot"></span>
    <span class="brand__name">Mentara</span>
  </div>
  <div class="person">
    <p class="person__name">Nome Sobrenome</p>
    <p class="person__role">cargo</p>
  </div>
  <span class="divider"></span>
  <ul class="contacts">
    <li>+55 21 3210-4780 <svg class="icon"><use href="#i-phone"/></svg></li>
    <li>/clinicamentara <svg class="icon"><use href="#i-social"/></svg></li>
    <li>R. Aurora Nº 24 - centro <svg class="icon"><use href="#i-pin"/></svg></li>
    <li>mentara.com.br <svg class="icon"><use href="#i-web"/></svg></li>
  </ul>
  <span class="base-band"></span>
</section>
</body>
</html>
```